We need a web design for a retail food business based in Greater Western Sydney Australia called Golden Lantern Chinese Restaurant. Basically just need a simple yet easily to navigate website to browse through a menu, gallery , brief description about us, opening hours.
Menu and Gallery will be constantly updated.
Will provide own images for gallery
Updates
Menu has been uploaded and some idea on the colours I would like on the site
Some additional pictures added to see what designs you guys can come up with . Thanks again
To All Designers,
Any extra fee on top of the designs that feels need to be charged, please let me know in advance
Reason: Extending Deadline as I have yet to find a design that I would like...Thanks guys
Target Market(s)
All groups
Industry/Entity Type
Business
Requirements
Must have
- Open minded to any designs
Nice to have
- Would like slideshow behind main logo.
Preferred light coloured site yet not too playful
Should not have
- Preferably no dark colours backgrounds

```html
<!DOCTYPE html>
<html lang="en">
<head>
<meta charset="utf-8">
<title>Golden Lantern Chinese Restaurant</title>
<link href="https://fonts.googleapis.com/css2?family=Shojumaru&family=Carlito&family=Arimo&display=swap" rel="stylesheet">
<style>
  :root {
    --wall-warm: #c9803f;
    --wall-deep: #6e3a22;
    --wall-gold: #e0b24a;
    --floor: #5a4a44;
    --sidebar-pink: rgba(250, 200, 214, 0.62);
    --logo-bg: #f6dbe3;
    --nav-title: #3b0e1e;
    --nav-sub: #2a1a1f;
    --panel-bg: rgba(20, 12, 10, 0.62);
    --panel-head: rgba(30, 20, 18, 0.35);
    --panel-text: #ffffff;
    --social: #f8c9d6;
    --chef-bg: #f1f1f1;
  }
  * { margin: 0; padding: 0; box-sizing: border-box; }
  html, body { width: 1200px; height: 673px; overflow: hidden; }
  body { position: relative; font-family: "Arimo", Arial, sans-serif; }

  .hero-scene {
    position: absolute; inset: 0;
    background:
      radial-gradient(ellipse 420px 260px at 800px 300px, rgba(240,170,90,0.55), transparent 70%),
      linear-gradient(180deg, #8a7a68 0%, #b98c55 22%, var(--wall-warm) 40%, var(--wall-gold) 55%, var(--wall-deep) 78%, var(--floor) 100%);
  }

  .site-logo {
    position: absolute; left: 119px; top: 0; width: 266px; height: 114px;
    background: var(--logo-bg);
    box-shadow: 0 3px 6px rgba(0,0,0,0.35);
    display: flex; align-items: center; justify-content: center;
    text-align: center; padding: 0 18px;
  }
  .site-logo__name {
    font-family: "Shojumaru", "Carlito", sans-serif;
    color: #a3182c; font-size: 19px; line-height: 1.25;
  }

  .sidebar { position: absolute; left: 119px; top: 114px; width: 266px; height: 510px; }
  .sidebar__shape { position: absolute; inset: 0; }

  .main-nav { position: absolute; left: 156px; top: 158px; list-style: none; }
  .main-nav__item { height: 81px; }
  .main-nav__title {
    display: block; font-family: "Shojumaru", cursive;
    color: var(--nav-title); font-size: 20px; line-height: 24px;
  }
  .main-nav__sub {
    display: block; font-family: "Carlito", "Calibri", sans-serif;
    color: var(--nav-sub); font-size: 11.5px; line-height: 12px;
  }

  .social-links { position: absolute; left: 986px; top: 4px; display: flex; gap: 4px; }
  .social-links__dot { width: 26px; height: 26px; border-radius: 50%; background: var(--social); }

  .welcome {
    position: absolute; left: 496px; top: 333px; width: 497px; height: 278px;
    background: var(--panel-bg); color: var(--panel-text);
  }
  .welcome__head {
    height: 48px; padding: 12px 0 0 30px; background: var(--panel-head);
    font-size: 19px; font-weight: 400;
  }
  .welcome__photo {
    position: absolute; left: 25px; top: 64px; width: 139px; height: 186px;
    background: linear-gradient(180deg, #ffffff 0%, var(--chef-bg) 60%, #e2dcd6 100%);
  }
  .welcome__copy {
    position: absolute; left: 196px; top: 66px; width: 280px;
    font-size: 13.4px; line-height: 16.5px;
  }
  .welcome__copy p + p { margin-top: 16px; }
</style>
</head>
<body>
  <div class="hero-scene" role="img" aria-label="Photo of the restaurant dining room with bar counter, tables and chairs"></div>

  <div class="sidebar">
    <svg class="sidebar__shape" width="266" height="510" viewBox="0 0 266 510" aria-hidden="true">
      <path d="M0 0 H266 V486 C210 430 70 430 0 504 Z" fill="var(--sidebar-pink)"/>
    </svg>
  </div>

  <header class="site-logo">
    <span class="site-logo__name">Golden Lantern Chinese Restaurant</span>
  </header>

  <nav>
    <ul class="main-nav">
      <li class="main-nav__item"><span class="main-nav__title">About Us</span><span class="main-nav__sub">More about us</span></li>
      <li class="main-nav__item"><span class="main-nav__title">Menu</span><span class="main-nav__sub">See our Menu</span></li>
      <li class="main-nav__item"><span class="main-nav__title">Gallery</span><span class="main-nav__sub">Enjoy our gallery</span></li>
      <li class="main-nav__item"><span class="main-nav__title">Opening Hours</span><span class="main-nav__sub">Visiting time</span></li>
      <li class="main-nav__item"><span class="main-nav__title">Contact Us</span><span class="main-nav__sub">Get in touch with us</span></li>
    </ul>
  </nav>

  <div class="social-links" aria-label="Social links">
    <span class="social-links__dot"></span>
    <span class="social-links__dot"></span>
    <span class="social-links__dot"></span>
  </div>

  <section class="welcome">
    <h1 class="welcome__head">Hello There !</h1>
    <div class="welcome__photo" role="img" aria-label="Photo of a smiling chef in a white hat"></div>
    <div class="welcome__copy">
      <p>Ut wisi enim ad minim veniam, quis nostrud exerci tation ullamcorper suscipit lobortis nisl ut aliquip ex ea commodo consequat.</p>
      <p>Duis autem vel eum iriure dolor in hendrerit in vulputate velit esse molestie consequat, vel illum dolore eu feugiat nulla facilisis at vero eros et accumsan et iusto odio dignissim.</p>
      <p>Qui blandit praesent luptatum zzril delenit augue duis dolore te feugait nulla facilisi.</p>
    </div>
  </section>
</body>
</html>
```